Visitenkarte und Briefpapier für Rechtsanwaltskanzlei
Zielgruppe
Neugründung einer Rechtsanwaltskanzlei für Strafrecht mit einem Anwalt
Aufgabenstellung
Ich möchte gerne Briefpapier und Visitenkarten mit einem schlichten aber professionellen Charakter für meine neue Rechtsanwaltskanzlei erstellen lassen. Die Erscheinung soll modern, sachlich und klar sein. Es soll kein Logo verwendet werden, sondern nur der Namensschriftzug "Dr. Harald Obst", gerne in Großbuchstaben. Siehe dazu beispielhaft die Design-Charakter der angegeben Links.
Die Visitenkarte sollen als druckfähiges PDF und das Briefpapier zusätzlich als Word-Dokument geliefert werden.

```html
<!DOCTYPE html>
<html lang="de">
<head>
<meta charset="utf-8">
<title>Dr. Harald Obst – Briefpapier und Visitenkarte</title>
<link rel="stylesheet" href="https://fonts.googleapis.com/css2?family=Oswald:wght@400;500&family=Open+Sans:wght@400&display=swap">
<style>
  :root {
    --backdrop: #e2e2e2;
    --paper: #ffffff;
    --band: #464646;
    --band-text: #ffffff;
    --body-text: #222222;
    --card-text: #555555;
  }
  * { margin: 0; padding: 0; box-sizing: border-box; }
  html, body {
    width: 1200px; height: 931px; overflow: hidden;
    background: var(--backdrop);
  }
  .stage { position: relative; width: 1200px; height: 931px; }

  /* Letterhead */
  .letterhead {
    position: absolute; left: 179px; top: 58px;
    width: 571px; height: 809px;
    background: var(--paper);
  }
  .letterhead__brand {
    position: absolute; left: 0; top: 25px;
    width: 182px; height: 35px;
    background: var(--band); color: var(--band-text);
    font-family: "Oswald", sans-serif; text-align: right;
    padding: 6px 32px 0 0;
  }
  .brand__name { font-size: 12px; font-weight: 500; line-height: 13px; letter-spacing: 0.2px; }
  .brand__role { font-size: 7.5px; line-height: 9px; }
  .letterhead__body {
    position: absolute; left: 54px; top: 97px; width: 490px;
    font-family: "Open Sans", sans-serif; font-size: 9.55px; line-height: 13.85px;
    color: var(--body-text);
  }
  .letter__salutation { margin-bottom: 27.7px; }
  .letter__paragraph { text-align: justify; margin-bottom: 13.85px; hyphens: manual; }
  .letterhead__footer {
    position: absolute; left: 0; bottom: 0; width: 571px; height: 36px;
    background: var(--band); color: var(--band-text);
    font-family: "Oswald", sans-serif; font-size: 7.6px;
    padding: 11px 0 0 54px; white-space: nowrap;
  }
  .letterhead__footer span { margin-right: 5px; }

  /* Business card */
  .business-card {
    position: absolute; left: 840px; top: 254px;
    width: 231px; height: 128px;
    background: var(--paper);
  }
  .business-card__brand {
    position: absolute; left: 0; top: 12px; width: 231px; height: 34px;
    background: var(--band); color: var(--band-text);
    font-family: "Oswald", sans-serif; text-align: right;
    padding: 6px 22px 0 0;
  }
  .business-card__contact {
    position: absolute; right: 20px; top: 68px;
    font-family: "Oswald", sans-serif; font-size: 5.4px; line-height: 13px;
    color: var(--card-text); text-align: right;
  }
  .business-card__contact span + span { margin-left: 4px; }
  .business-card__stripe {
    position: absolute; left: 0; bottom: 0; width: 231px; height: 6px;
    background: var(--band);
  }
</style>
</head>
<body>
<main class="stage">

  <article class="letterhead">
    <header class="letterhead__brand">
      <div class="brand__name">DR. HARALD OBST</div>
      <div class="brand__role">Rechtsanwalt</div>
    </header>

    <section class="letterhead__body">
      <p class="letter__salutation">Lorem ipsum dolor sit amet,</p>
      <p class="letter__paragraph">Lorem ipsum dolor sit amet, consetetur sadipscing elitr, sed diam nonumy eirmod tempor invidunt ut labore et dolore magna aliquyam erat, sed diam voluptua. At vero eos et accusam et justo duo dolores et ea rebum. Stet clita kasd gubergren, no sea takimata sanctus est Lorem ipsum dolor sit amet. Lorem ipsum dolor sit amet, consetetur sadipscing elitr, sed diam nonumy eirmod tempor invidunt ut labore et dolore magna aliquyam erat, sed diam voluptua. At vero eos et accusam et justo duo dolores et ea rebum. Stet clita kasd gubergren, no sea takimata sanctus est Lorem ipsum dolor sit amet. Lorem ipsum dolor sit amet, consetetur sadipscing elitr, sed diam nonumy eirmod tempor invidunt ut labore et dolore magna aliquyam erat, sed diam voluptua. At vero eos et accusam et justo duo dolores et ea rebum. Stet clita kasd gubergren, no sea takimata sanctus est Lorem ipsum dolor sit amet.</p>
      <p class="letter__paragraph">Duis autem vel eum iriure dolor in hendrerit in vulputate velit esse molestie consequat, vel illum dolore eu feugiat nulla facilisis at vero eros et accumsan et iusto odio dignissim qui blandit praesent luptatum zzril delenit augue duis dolore te feugait nulla facilisi. Lorem ipsum dolor sit amet, consectetuer adipiscing elit, sed diam nonummy nibh euismod tincidunt ut laoreet dolore magna aliquam erat volutpat.</p>
      <p class="letter__paragraph">Ut wisi enim ad minim veniam, quis nostrud exerci tation ullamcorper suscipit lobortis nisl ut aliquip ex ea commodo consequat. Duis autem vel eum iriure dolor in hendrerit in vulputate velit esse molestie conse&shy;quat, vel illum dolore eu feugiat nulla facilisis at vero eros et accumsan et iusto odio dignissim qui blandit praesent luptatum zzril delenit augue duis dolore te feugait nulla facilisi.</p>
      <p class="letter__paragraph">Nam liber tempor cum soluta nobis eleifend option congue nihil imperdiet doming id quod mazim placerat facer possim assum. Lorem ipsum dolor sit amet, consectetuer adipiscing elit, sed diam nonummy nibh euismod tincidunt ut laoreet dolore magna aliquam erat volutpat. Ut wisi enim ad minim veniam, quis nostrud exerci tation ullamcorper suscipit lobortis nisl ut aliquip ex ea commodo consequat.</p>
      <p class="letter__paragraph">Duis autem vel eum iriure dolor in hendrerit in vulputate velit esse molestie consequat, vel illum dolore eu feugiat nulla facilisis.</p>
      <p class="letter__paragraph">At vero eos et accusam et justo duo dolores et ea rebum. Stet clita kasd gubergren, no sea takimata sanctus est Lorem ipsum dolor sit amet. Lorem ipsum dolor sit amet, consetetur sadipscing elitr, sed diam nonumy eirmod tempor invidunt ut labore et dolore magna aliquyam erat, sed diam voluptua. At vero eos et accusam et justo duo dolores et ea rebum. Stet clita kasd gubergren, no sea takimata sanctus est Lorem ipsum dolor sit amet. Lorem ipsum dolor sit amet, consetetur sadipscing elitr, At accusam aliquyam diam diam dolore dolores duo eirmod eos erat, et nonumy sed tempor et et invidunt justo labore Stet clita ea et gubergren, kasd magna no rebum. sanctus sea sed takimata ut vero voluptua. est Lorem ipsum dolor sit amet. Lorem ipsum dolor sit amet, consetetur sadipscing elitr, sed diam nonumy eirmod tempor invidunt ut labore et dolore magna aliquyam erat.</p>
    </section>

    <footer class="letterhead__footer">
      <span>Lindenhofweg 7, 80331 München, Deutschland</span>
      <span>T: +49 0987 65432100</span>
      <span>F: +49 0987 65432101</span>
      <span>info@harald-obst.de</span>
      <span>www.harald-obst.de</span>
    </footer>
  </article>

  <aside class="business-card">
    <header class="business-card__brand">
      <div class="brand__name">DR. HARALD OBST</div>
      <div class="brand__role">Rechtsanwalt</div>
    </header>
    <div class="business-card__contact">
      <div>Lindenhofweg 7, 80331 München, Deutschland</div>
      <div><span>T: +49 0987 65432100</span><span>F: +49 0987 65432101</span></div>
      <div><span>info@harald-obst.de</span><span>www.harald-obst.de</span></div>
    </div>
    <div class="business-card__stripe"></div>
  </aside>

</main>
</body>
</html>
```